Steel Company / Iron Railing Business Card Template

We are a custom steel fabrication company located in Marlow Glen, PA. In business since 1979, we recently developed a new logo, and we're looking for a business card design to help display the new logo and our business. The name of the company is Kelbrook Forge Co.. The Office Phone number is (610) 555-0143. We fabricate and install custom "wrought iron" railings on our residential side, we also fabricate and erect structural steel (think cranes and steel beams in buildings) on our commercial side. Looking to get a business card template designed. Something modern, but professional. Clear and easy to read. Front should have all business and employee information including phone number(s), email address, business information, etc. back should spotlight logo.

Industry/Entity Type

Construction / Home Improvement

Contact Information for Business Card

Business information is Kelbrook Forge Co., 48 Dunmore Ave Suite 3305, Marlow Glen, PA 19074. Phone number is (610) 555-0143. Website is www.kelbrookforge.example Business card should be for "Tom Pelling" with the job title "Sales & Estimating" but be editable for other employees. Tom's phone number is (610) 555-0178

Colors

Designer to choose colors to be used in the design.

Requirements
Must have
• Modern Feel, Design should be sized for standard business card sizing 3.5" x 2" (88.9mm x 50.8mm)

```html
<!DOCTYPE html>
<html lang="en">
<head>
<meta charset="utf-8">
<title>Kelbrook Forge Co. – Business Card</title>
<link href="https://fonts.googleapis.com/css2?family=Oswald:wght@600&family=Poppins:wght@400;600;700&display=swap" rel="stylesheet">
<style>
  :root {
    --page-bg: #1c1c1c;
    --card-dark: #0b0b0c;
    --card-mid: #1f2022;
    --brand-blue: #2a44a8;
    --brand-red: #d8232a;
    --text-light: #f2f2f2;
    --emboss: #2a2b2e;
  }
  * { box-sizing: border-box; margin: 0; padding: 0; }
  html, body {
    width: 1200px; height: 1015px; overflow: hidden;
    background: var(--page-bg);
    font-family: "Poppins", sans-serif;
  }
  .sheet {
    width: 1200px; height: 1015px;
    display: flex; flex-direction: column; align-items: center; justify-content: center;
    gap: 45px;
  }
  .card {
    position: relative;
    width: 770px; height: 440px;
    background: linear-gradient(160deg, var(--card-mid) 0%, var(--card-dark) 45%, #151517 70%, var(--card-dark) 100%);
    box-shadow: 0 14px 30px rgba(0,0,0,.55);
    overflow: hidden;
  }
  .card::after {
    content: ""; position: absolute; left: 0; right: 0; bottom: 0; height: 7px;
    background: var(--brand-red);
  }

  /* Back */
  .card-back { display: flex; align-items: center; justify-content: center; }
  .back-mark { display: flex; align-items: center; gap: 18px; }
  .back-mark .mark-dot { width: 54px; height: 54px; border-radius: 50%; background: var(--emboss); }
  .back-mark .mark-name { font-weight: 700; font-size: 46px; color: var(--emboss); letter-spacing: .5px; }

  /* Front */
  .front-mark {
    position: absolute; right: 60px; top: 60px;
    display: flex; align-items: center; gap: 14px;
  }
  .front-mark .mark-dot { width: 46px; height: 46px; border-radius: 50%; background: var(--brand-red); }
  .front-mark .mark-name { font-weight: 700; font-size: 36px; color: var(--brand-blue); }

  .employee {
    position: absolute; left: 54px; top: 150px;
    padding-left: 26px;
  }
  .employee::before {
    content: ""; position: absolute; left: 0; top: 30px; width: 16px; height: 66px;
    background: var(--brand-red);
  }
  .employee-name {
    font-family: "Oswald", sans-serif; font-weight: 600;
    font-size: 32px; line-height: 1.05; color: var(--brand-blue);
    text-transform: uppercase; letter-spacing: .5px;
  }
  .employee-title { font-size: 23px; color: var(--brand-red); line-height: 1.3; }

  .contact-line {
    display: flex; align-items: center; gap: 10px;
    font-size: 22px; color: var(--text-light); line-height: 1.35;
  }
  .contact-line svg { width: 20px; height: 20px; flex: none; }
  .icon-fill { fill: var(--brand-blue); }
  .icon-line { fill: none; stroke: var(--brand-blue); stroke-width: 2; stroke-linejoin: round; }

  .address {
    position: absolute; right: 60px; top: 200px;
    text-align: right; font-size: 21px; line-height: 1.3; color: var(--text-light);
  }
  .address .company { color: var(--brand-blue); font-weight: 600; font-size: 20px; }

  .office-contacts { position: absolute; left: 120px; bottom: 50px; }
</style>
</head>
<body>
<main class="sheet">

  <section class="card card-back" aria-label="Card back">
    <div class="back-mark">
      <span class="mark-dot"></span>
      <span class="mark-name">Kelbrook Forge Co.</span>
    </div>
  </section>

  <section class="card card-front" aria-label="Card front">
    <div class="front-mark">
      <span class="mark-dot"></span>
      <span class="mark-name">Kelbrook Forge Co.</span>
    </div>

    <div class="employee">
      <p class="employee-name">Tom Pelling</p>
      <p class="employee-title">Sales &amp; Estimating</p>
      <p class="contact-line">
        <svg class="icon-fill" viewBox="0 0 24 24"><path d="M6.6 10.8a15.1 15.1 0 0 0 6.6 6.6l2.2-2.2c.3-.3.7-.4 1-.2 1.1.4 2.3.6 3.6.6.6 0 1 .4 1 1V20c0 .6-.4 1-1 1A17 17 0 0 1 3 4c0-.6.4-1 1-1h3.5c.6 0 1 .4 1 1 0 1.3.2 2.5.6 3.6.1.3 0 .7-.2 1z"/></svg>
        (610) 555-0178
      </p>
    </div>

    <div class="address">
      <p class="company">Kelbrook Forge Co.</p>
      <p>48 Dunmore Ave Suite 3305</p>
      <p>Marlow Glen, PA 19074</p>
    </div>

    <div class="office-contacts">
      <p class="contact-line">
        <svg class="icon-fill" viewBox="0 0 24 24"><path d="M6.6 10.8a15.1 15.1 0 0 0 6.6 6.6l2.2-2.2c.3-.3.7-.4 1-.2 1.1.4 2.3.6 3.6.6.6 0 1 .4 1 1V20c0 .6-.4 1-1 1A17 17 0 0 1 3 4c0-.6.4-1 1-1h3.5c.6 0 1 .4 1 1 0 1.3.2 2.5.6 3.6.1.3 0 .7-.2 1z"/></svg>
        (610) 555-0143
      </p>
      <p class="contact-line">
        <svg class="icon-line" viewBox="0 0 24 24"><rect x="3" y="5" width="18" height="14"/><path d="M3 5l9 7 9-7"/></svg>
        info@kelbrookforge.example
      </p>
      <p class="contact-line">
        <svg class="icon-line" viewBox="0 0 24 24"><circle cx="12" cy="12" r="9"/><ellipse cx="12" cy="12" rx="4" ry="9"/><path d="M3 12h18"/></svg>
        www.kelbrookforge.example
      </p>
    </div>
  </section>

</main>
</body>
</html>
```